TRV Insurance - Letterhead

We need a corporate letterhead template (word) and slide show template (PowerPoint) designed for our Insurance Business.
TRV Insurance is in the insurance industry. Please visit our website www.trvinsurance-example.com
Both templates (word and PowerPoint) must include the TRV logo (attached to this project) and can be very similar in design.
We are after something creative yet professional in design.
Please feel free to ask any questions.

```html
<!DOCTYPE html>
<html lang="en">
<head>
<meta charset="utf-8">
<title>TRV Insurance – Letterhead</title>
<link rel="stylesheet" href="https://fonts.googleapis.com/css2?family=Questrial&family=Arimo:wght@400;700&display=swap">
<style>
  :root {
    --backdrop: #ebebeb;
    --paper: #fbfbfb;
    --paper-edge: #d4d4d4;
    --ink: #1f1f1f;
    --body-ink: #3a3a3a;
    --muted: #555555;
    --rule: #bdbdbd;
    --orange: #e8581c;
    --yellow: #f2c300;
    --navy: #23318c;
    --signature-blue: #8a95c9;
  }
  * { box-sizing: border-box; margin: 0; padding: 0; }
  html, body { width: 1200px; height: 815px; overflow: hidden; }
  body { background: var(--backdrop); position: relative; font-family: "Arimo", Arial, sans-serif; color: var(--body-ink); }

  .sheet {
    position: absolute; top: 72px; width: 482px; height: 680px;
    background: var(--paper);
    border-bottom: 10px solid var(--paper-edge);
  }
  .sheet--letter { left: 80px; }
  .sheet--blank { left: 638px; }

  .brand { position: absolute; left: 55px; top: 44px; display: flex; align-items: flex-start; gap: 6px; }
  .brand__dot { width: 13px; height: 13px; border-radius: 50%; background: var(--orange); margin-top: 4px; }
  .brand__name { font-family: "Questrial", sans-serif; color: var(--ink); line-height: 1; }
  .brand__name-main { display: block; font-size: 27px; letter-spacing: 0.5px; }
  .brand__name-sub { display: block; font-size: 15px; letter-spacing: 0.6px; margin-top: 1px; }

  .letter { position: absolute; left: 55px; top: 218px; width: 373px; }
  .letter__salutation { font-family: "Arimo", sans-serif; font-weight: 700; font-size: 9.5px; color: var(--ink); margin-bottom: 10px; }
  .letter__para { font-size: 7.3px; line-height: 11.3px; text-align: justify; margin-bottom: 9px; }
  .letter__para--indent { text-indent: 8px; }

  .signoff { position: absolute; left: 260px; top: 410px; width: 168px; height: 52px; }
  .signoff__signature { position: absolute; left: 0; top: 0; width: 105px; height: 50px; background: linear-gradient(90deg, transparent, rgba(138,149,201,0.35), transparent); border-radius: 20px; }
  .signoff__closing { position: absolute; right: 0; top: 4px; font-size: 7.3px; text-align: right; }
  .signoff__name { position: absolute; right: 0; top: 17px; font-size: 8.5px; font-weight: 700; color: var(--ink); }

  .footer { position: absolute; left: 52px; top: 622px; display: flex; align-items: flex-start; font-size: 6.8px; color: var(--muted); }
  .footer__contacts { list-style: none; }
  .footer__contacts li { display: flex; align-items: center; gap: 5px; height: 9.3px; }
  .footer__icon { width: 7px; height: 7px; border-radius: 50%; display: inline-block; }
  .footer__icon--phone { background: var(--orange); }
  .footer__icon--mail { background: var(--yellow); }
  .footer__icon--web { background: var(--navy); }
  .footer__divider { width: 1px; height: 18px; background: var(--rule); margin: 5px 13px 0 14px; }
  .footer__address { font-style: normal; line-height: 9.3px; padding-top: 9px; }
</style>
</head>
<body>

<section class="sheet sheet--letter">
  <header class="brand">
    <span class="brand__dot"></span>
    <span class="brand__name"><span class="brand__name-main">TRV</span><span class="brand__name-sub">INSURANCE</span></span>
  </header>

  <article class="letter">
    <p class="letter__salutation">Dear sir / madame,</p>
    <p class="letter__para">Lorem ipsum dolor sit amet, consectetur adipisicing elit, sed do eiusmod tempor incididunt ut labore et dolore magna aliqua. Ut enim ad minim veniam, quis nostrud exercitation ullamco laboris nisi ut aliquip ex ea commodo consequat. Duis aute irure dolor in reprehenderit in voluptate velit esse cillum dolore eu fugiat nulla pariatur. Excepteur sint occaecat cupidatat non proident, sunt in culpa qui officia deserunt mollit anim id est laborum.Lorem ipsum dolor sit amet, consectetur adipisicing elit, sed do eiusmod tempor incididunt ut labore et dolore magna aliqua. Ut enim ad minim veniam, quis nostrud exercitation ullamco laboris nisi ut aliquip ex ea commodo consequat. Duis aute irure dolor in reprehenderit in voluptate velit esse cillum dolore eu fugiat nulla pariatur. Excepteur sint occaecat cupidatat non proident, sunt in culpa qui officia deserunt mollit anim id est laborum.</p>
    <p class="letter__para letter__para--indent">Lorem ipsum dolor sit amet, consectetur adipisicing elit, sed do eiusmod tempor incididunt ut labore et dolore magna aliqua. Ut enim ad minim veniam, quis nostrud exercitation ullamco laboris nisi ut aliquip ex ea commodo consequat. Duis aute irure dolor in reprehenderit in voluptate velit esse cillum dolore eu fugiat nulla pariatur. Excepteur sint occaecat cupidatat non proident, sunt in culpa qui officia deserunt mollit anim id est laborum.</p>
  </article>

  <div class="signoff">
    <div class="signoff__signature" role="img" aria-label="Handwritten signature of the sender"></div>
    <p class="signoff__closing">Yours Sincerely,</p>
    <p class="signoff__name">Dana Kellet</p>
  </div>

  <footer class="footer">
    <ul class="footer__contacts">
      <li><span class="footer__icon footer__icon--phone"></span>1300 555 210</li>
      <li><span class="footer__icon footer__icon--mail"></span>info@trvinsurance-example.com</li>
      <li><span class="footer__icon footer__icon--web"></span>www.trvinsurance-example.com</li>
    </ul>
    <span class="footer__divider"></span>
    <address class="footer__address">Po Box 118<br>Northvale VIC 3990</address>
  </footer>
</section>

<section class="sheet sheet--blank">
  <header class="brand">
    <span class="brand__dot"></span>
    <span class="brand__name"><span class="brand__name-main">TRV</span><span class="brand__name-sub">INSURANCE</span></span>
  </header>

  <footer class="footer">
    <ul class="footer__contacts">
      <li><span class="footer__icon footer__icon--phone"></span>1300 555 210</li>
      <li><span class="footer__icon footer__icon--mail"></span>info@trvinsurance-example.com</li>
      <li><span class="footer__icon footer__icon--web"></span>www.trvinsurance-example.com</li>
    </ul>
    <span class="footer__divider"></span>
    <address class="footer__address">Po Box 118<br>Northvale VIC 3990</address>
  </footer>
</section>

</body>
</html>
```